Up and Coming Granola Brand Needs Labels and Logo Design

We need a label design for a new Granola Company called Pem's Granola. We create delicious hand-crafted granolas that are not only tasty, but good for you!

We would also like a 'modern' logo, similar to the attached one.
The logo name is "Pem's". The concept would be to have the word "Pem's" in the banner, and "Granola" below in font. Eventually the product line will expand to include other items, and we would like a logo that allows us to match the product to the logo name.

The logo should integrate well with the packaging label.

We plan on using light brown resealable packaging for our granola, and would prefer earthy colours, or colours that would complement the packaging for the labels. We intend to print the designs on labels, and paste them on the front and back of the package. (Package dimensions and image of package are included in attachments)

We plan on having a few flavours of Granola, and that would have some small changes on the label design.

Some of our ingredients in our granola would include Oats, Dried fruit, nuts and various grains.

It would be good if the labels could feature oats (perhaps an ear of oats, or something to similar effect)
Updates

have added dimensions to the packaging to give a sense of size for reference. image of the packaging we will be using also added! Added Wednesday, May 11, 2016

Reason: Loving the submissions so far! Can't wait to see what else you can come up with! Have extended the deadline to give some breathing room and time for tweaking!

Target Market(s)

20s-40s

Industry/Entity Type

Food Store

Logo Text

Pem's

Font styles to use
Serif
Decorative

Requirements
Must have
• -Colours that complement the packaging colour (light brown)
• -Can be printed on white labels that will be stuck on the packaging (both for the front of packaging; that has a window, and the back of the packaging; no window)
• -simple and stylish design that entices buyers to purchase the product
• -A flexible logo that can transition seamlessly between different product lines
• - Sections for "our story", "nutritional information", "ingredients, etc on the back label.
Nice to have
• -as attached in image samples for the brief.
• - other trendy designs that are currently popular
• - different colour schemes for different flavours. Currently there are 3 flavours; 1) Mocha Almond, 2) Matcha with White Chocolate and Cashews, and 3) Classic Fruit and Nut.
Should not have
• -colours that stand out too much, or do not fit the design brief
• -overly complicated designs that take away from the main theme of awesome granola

```html
<!DOCTYPE html>
<html lang="en">
<head>
<meta charset="UTF-8">
<title>Pem's Granola – Label Set</title>
<link href="https://fonts.googleapis.com/css2?family=Oswald:wght@400;500;600&family=Arimo:wght@700&family=Pinyon+Script&display=swap" rel="stylesheet">
<style>
  :root {
    --coral: #f2896a;
    --coral-light: #f6a88a;
    --lime: #dde562;
    --lime-light: #ecef9a;
    --sky: #4ea4cb;
    --sky-light: #8cc6df;
    --panel: #3a3735;
    --cream: #e6cfc0;
    --sand: #f1e3b8;
    --leaf: #6fb43a;
    --orange-red: #f0582a;
    --matcha: #d9e234;
    --mocha-blue: #2fa3dd;
    --white: #ffffff;
    --ink: #2b2b2b;
    --dot: #8c8782;
  }
  * { box-sizing: border-box; margin: 0; padding: 0; }
  html, body { width: 1200px; height: 1200px; overflow: hidden; background: var(--white); }
  .sheet { position: relative; width: 1200px; height: 1200px; }

  .coral { --bg: var(--coral); --bg-light: var(--coral-light); --accent: var(--orange-red); }
  .lime  { --bg: var(--lime);  --bg-light: var(--lime-light);  --accent: var(--matcha); }
  .sky   { --bg: var(--sky);   --bg-light: var(--sky-light);   --accent: var(--mocha-blue); }

  /* ---------- front label ---------- */
  .front-label {
    position: absolute; border-radius: 8px; overflow: hidden; background: var(--bg);
  }
  .front-label .field {
    position: absolute; left: 0; right: 0; bottom: 0; height: 60%;
    background: linear-gradient(180deg, transparent 0%, var(--bg-light) 55%, var(--sand) 100%);
  }
  .front-label .oats-left, .front-label .oats-right {
    position: absolute; bottom: 0; width: 24%; height: 62%;
    background: linear-gradient(180deg, transparent, rgba(201,138,60,.45));
  }
  .front-label .oats-left { left: 0; }
  .front-label .oats-right { right: 0; }
  .brand-line {
    position: absolute; left: 0; right: 0; top: 7%;
    text-align: center; white-space: nowrap;
    font-family: 'Oswald', sans-serif; font-weight: 600; font-size: 32px; line-height: 1;
    color: var(--panel);
  }
  .badge { position: absolute; left: 24%; width: 54%; top: 28%; bottom: 0; }
  .badge svg { position: absolute; inset: 0; width: 100%; height: 100%; }
  .badge-content {
    position: absolute; left: 6%; right: 6%; top: 7%;
    text-align: center; font-family: 'Oswald', sans-serif; white-space: nowrap;
  }
  .tagline {
    color: #e9e2d8; font-size: 12px; font-weight: 400; line-height: 1.2;
    padding-bottom: 5px; border-bottom: 2px solid var(--leaf);
  }
  .flavour { margin-top: 6px; color: var(--accent); font-weight: 500; line-height: 1; }
  .flavour span { display: block; }
  .flavour .big { font-size: 42px; }
  .flavour .mid { font-size: 32px; }
  .flavour .link { font-size: 12px; color: var(--leaf); line-height: 1; }
  .flavour .white { font-size: 20px; color: var(--white); }
  .dots { margin-top: 6px; height: 6px; border-top: 2px dotted var(--dot); border-bottom: 2px solid var(--leaf); }

  /* ---------- back label ---------- */
  .back-label { position: absolute; border-radius: 8px; overflow: hidden; background: var(--bg); }
  .back-label .wash {
    position: absolute; left: 0; right: 0; bottom: 0; height: 40%;
    background: linear-gradient(180deg, transparent, var(--bg-light) 60%, var(--sand));
  }
  .story-panel {
    position: absolute; left: 3%; top: 3%; width: 49%; height: 91%;
    background: var(--panel); border-radius: 12px; overflow: hidden;
  }
  .story-oats {
    position: absolute; left: 0; right: 0; top: 35%; bottom: 0;
    background: linear-gradient(180deg, transparent, rgba(201,138,60,.14) 60%, rgba(201,138,60,.06));
  }
  .story-title {
    position: absolute; left: 7%; top: 2%;
    font-family: 'Pinyon Script', cursive; color: var(--leaf); font-size: 28px; white-space: nowrap;
  }
  .story-foot {
    position: absolute; left: 4%; right: 4%; bottom: 6%;
    text-align: center; font-family: 'Oswald', sans-serif; color: var(--white); white-space: nowrap;
  }
  .story-foot .mini-brand { font-size: 16px; font-weight: 600; line-height: 1; }
  .story-foot .rule { border-top: 2px dotted var(--dot); margin: 9px 0; }
  .story-foot .web { font-size: 12px; }
  .nutrition {
    position: absolute; left: 54%; right: 3%; top: 3%; height: 66%;
    background: var(--cream);
  }
  .nutrition h2 {
    font-family: 'Arimo', sans-serif; font-size: 16px; color: var(--ink);
    padding: 6px 10px; white-space: nowrap;
  }
  .nutrition .ingredients {
    position: absolute; left: 10px; top: 55%;
    font-family: 'Arimo', sans-serif; font-size: 8px; color: var(--ink);
  }
  .upc {
    position: absolute; left: 54%; right: 4%; bottom: 6%; height: 17%;
    background: var(--white); border: 1px solid #555;
    display: flex; align-items: center; justify-content: center;
    font-family: 'Oswald', sans-serif; font-size: 13px; color: var(--ink);
  }
</style>
</head>
<body>
<main class="sheet">

  <!-- Classic Fruit & Nut : front -->
  <section class="front-label coral" style="left:39px; top:153px; width:323px; height:260px;">
    <div class="field" role="img" aria-label="Soft field of oat stalks"></div>
    <div class="oats-left" role="img" aria-label="Ears of oats"></div>
    <div class="oats-right" role="img" aria-label="Ears of oats"></div>
    <p class="brand-line">Pem's Granola</p>
    <div class="badge">
      <svg viewBox="0 0 100 100" preserveAspectRatio="none"><polygon points="1,0 99,0 99,100 50,88 1,100" fill="var(--panel)" stroke="#fff" stroke-width="2" vector-effect="non-scaling-stroke"/></svg>
      <div class="badge-content">
        <p class="tagline">not only tasty, but good for you!</p>
        <p class="flavour"><span class="big">CLASSIC</span><span class="mid">FRUIT &amp; NUT</span></p>
        <div class="dots"></div>
      </div>
    </div>
  </section>

  <!-- Classic Fruit & Nut : back -->
  <section class="back-label coral" style="left:390px; top:92px; width:344px; height:420px;">
    <div class="wash"></div>
    <div class="story-panel">
      <div class="story-oats" role="img" aria-label="Faint oat stalks"></div>
      <p class="story-title">Our Story</p>
      <div class="story-foot">
        <p class="mini-brand">Pem's Granola</p>
        <div class="rule"></div>
        <p class="web">www.pemsgranola.example</p>
        <div class="rule"></div>
      </div>
    </div>
    <div class="nutrition"><h2>Nutrition Facts</h2><p class="ingredients">INGREDIENTS:</p></div>
    <div class="upc">UPC Code</div>
  </section>

  <!-- Mocha Almond : front -->
  <section class="front-label sky" style="left:802px; top:120px; width:322px; height:250px;">
    <div class="field" role="img" aria-label="Soft field of oat stalks"></div>
    <div class="oats-left" role="img" aria-label="Ears of oats"></div>
    <div class="oats-right" role="img" aria-label="Ears of oats"></div>
    <p class="brand-line">Pem's Granola</p>
    <div class="badge">
      <svg viewBox="0 0 100 100" preserveAspectRatio="none"><polygon points="1,0 99,0 99,100 50,88 1,100" fill="var(--panel)" stroke="#fff" stroke-width="2" vector-effect="non-scaling-stroke"/></svg>
      <div class="badge-content">
        <p class="tagline">not only tasty, but good for you!</p>
        <p class="flavour"><span class="big">MOCHA</span><span class="mid">Almond</span></p>
        <div class="dots"></div>
      </div>
    </div>
  </section>

  <!-- Matcha with White Chocolate and Cashews : front -->
  <section class="front-label lime" style="left:41px; top:754px; width:335px; height:272px;">
    <div class="field" role="img" aria-label="Soft field of oat stalks"></div>
    <div class="oats-left" role="img" aria-label="Ears of oats"></div>
    <div class="oats-right" role="img" aria-label="Ears of oats"></div>
    <p class="brand-line">Pem's Granola</p>
    <div class="badge">
      <svg viewBox="0 0 100 100" preserveAspectRatio="none"><polygon points="1,0 99,0 99,100 50,92 1,100" fill="var(--panel)" stroke="#fff" stroke-width="2" vector-effect="non-scaling-stroke"/></svg>
      <div class="badge-content" style="top:5%;">
        <p class="tagline">not only tasty, but good for you!</p>
        <p class="flavour"><span class="big" style="font-size:38px;">MATCHA</span><span class="link">with</span><span class="white">WHITE CHOCOLATE</span><span class="link">and</span><span class="mid" style="font-size:30px;">CASHEWS</span></p>
        <div class="dots" style="border-bottom:none;"></div>
      </div>
    </div>
  </section>

  <!-- Matcha : back -->
  <section class="back-label lime" style="left:392px; top:690px; width:339px; height:412px;">
    <div class="wash"></div>
    <div class="story-panel">
      <div class="story-oats" role="img" aria-label="Faint oat stalks"></div>
      <p class="story-title">Our Story</p>
      <div class="story-foot">
        <p class="mini-brand">Pem's Granola</p>
        <div class="rule"></div>
        <p class="web">www.pemsgranola.example</p>
        <div class="rule"></div>
      </div>
    </div>
    <div class="nutrition"><h2>Nutrition Facts</h2><p class="ingredients">INGREDIENTS:</p></div>
    <div class="upc">UPC Code</div>
  </section>

  <!-- Mocha Almond : back -->
  <section class="back-label sky" style="left:808px; top:638px; width:310px; height:380px;">
    <div class="wash"></div>
    <div class="story-panel">
      <div class="story-oats" role="img" aria-label="Faint oat stalks"></div>
      <p class="story-title">Our Story</p>
      <div class="story-foot">
        <p class="mini-brand">Pem's Granola</p>
        <div class="rule"></div>
        <p class="web">www.pemsgranola.example</p>
        <div class="rule"></div>
      </div>
    </div>
    <div class="nutrition"><h2 style="font-size:15px;">Nutrition Facts</h2><p class="ingredients">INGREDIENTS:</p></div>
    <div class="upc">UPC Code</div>
  </section>

</main>
</body>
</html>
```